New Logo and Business Card

Want new logo and business card for multi brand website. Attached are the logos for the back of the card.
We want a new logo for the front, the name "Tallvisto" as the company name.
The logo can just be an "O" and a "B" for simplicity. With the text "Tallvisto" after it.
For the business card use this info:
Dale Furnow, PEng MBA
President
dale.furnow@tallvisto.ca
+14035512839
Industry/Entity Type
Business
Logo Text
Tallvisto
Logo styles of interest
Lettermark Logo

```html
<!DOCTYPE html>
<html lang="en">
<head>
<meta charset="utf-8">
<title>Tallvisto — Business Card</title>
<link rel="stylesheet" href="https://fonts.googleapis.com/css2?family=Alfa+Slab+One&family=Arvo:wght@700&display=swap">
<style>
  :root {
    --card-bg: #231f20;
    --ink-grey: #a5a7aa;
  }
  * { margin: 0; padding: 0; box-sizing: border-box; }
  html, body {
    width: 1200px;
    height: 686px;
    overflow: hidden;
    background: var(--card-bg);
  }
  .card {
    position: relative;
    width: 1200px;
    height: 686px;
    background: var(--card-bg);
    overflow: hidden;
  }
  .brand-disc {
    position: absolute;
    left: 0;
    top: 0;
  }
  .company-name {
    position: absolute;
    left: 789px;
    top: 228px;
    font-family: "Alfa Slab One", Georgia, serif;
    font-size: 50px;
    line-height: 1;
    color: var(--ink-grey);
    letter-spacing: 0.5px;
  }
  .contact {
    position: absolute;
    left: 795px;
    top: 317px;
    list-style: none;
    font-family: "Arvo", Georgia, serif;
    font-weight: 700;
    font-size: 25px;
    line-height: 34px;
    color: var(--ink-grey);
  }
</style>
</head>
<body>
  <main class="card">
    <svg class="brand-disc" width="400" height="686" viewBox="0 0 400 686" aria-hidden="true">
      <circle cx="140" cy="348" r="240" fill="var(--ink-grey)"/>
    </svg>

    <h1 class="company-name">Tallvisto</h1>

    <ul class="contact">
      <li class="contact-name">Dale Furnow, PEng MBA</li>
      <li class="contact-title">President</li>
      <li class="contact-email">dale.furnow@tallvisto.ca</li>
      <li class="contact-phone">+14035512839</li>
    </ul>
  </main>
</body>
</html>
```